Business Card Design - Law Firm

I need a business card design. I have attached a picture of the law firm's website and logo. The business card design should be consistent with those pictures. There should be a place for the employee name, employee job title, telephone number, facsimile number, address, website url, and email address for each employee.
Industry/Entity Type
Business

```html
<!DOCTYPE html>
<html lang="en">
<head>
<meta charset="utf-8">
<title>Marlowe Law – Business Cards</title>
<link rel="stylesheet" href="https://fonts.googleapis.com/css2?family=Open+Sans:wght@400;600&display=swap">
<style>
  :root {
    --backdrop: #1f1f21;
    --card: #ffffff;
    --ink: #2b2b2b;
    --ink-soft: #555555;
    --gold: #b59a3c;
    --gold-light: #d9bf5c;
    --mark: #151515;
    --rule: #c9c9c9;
    --band-grey: #4a4a4c;
  }
  * { margin: 0; padding: 0; box-sizing: border-box; }
  html, body {
    width: 1200px; height: 944px; overflow: hidden;
    background: var(--backdrop);
    font-family: "Open Sans", Arial, sans-serif;
    color: var(--ink);
  }
  .canvas { position: relative; width: 1200px; height: 944px; }

  .card {
    position: absolute;
    width: 700px; height: 400px;
    background: var(--card);
    border-radius: 26px;
    overflow: hidden;
    box-shadow: 0 10px 30px rgba(0,0,0,.45);
  }
  .card--front { left: 140px; top: 56px; }
  .card--back  { left: 360px; top: 488px; }

  /* brand lockup */
  .brand { position: absolute; display: flex; align-items: center; }
  .brand__mark { background: var(--mark); flex: none; }
  .brand__divider { width: 1px; background: var(--rule); flex: none; }
  .brand__name { color: var(--gold); font-weight: 400; white-space: nowrap; }

  .card--front .brand { left: 92px; top: 110px; }
  .card--front .brand__mark { width: 96px; height: 96px; }
  .card--front .brand__divider { height: 112px; margin: 0 26px; }
  .card--front .brand__name { font-size: 48px; letter-spacing: .5px; }

  .front__url {
    position: absolute; left: 0; right: 0; top: 290px;
    text-align: center; font-size: 17px; letter-spacing: 2px; color: var(--ink);
  }

  .card--back .brand { left: 46px; top: 42px; }
  .card--back .brand__mark { width: 56px; height: 56px; }
  .card--back .brand__divider { height: 66px; margin: 0 14px; }
  .card--back .brand__name { font-size: 28px; }

  .person { position: absolute; right: 44px; top: 52px; text-align: left; }
  .person__name { font-size: 25px; font-weight: 400; color: var(--ink); }
  .person__title { font-size: 15px; color: var(--gold); margin-left: 44px; }

  .address, .contacts {
    position: absolute; top: 222px; font-size: 16px; line-height: 22px; color: var(--ink-soft);
  }
  .address { left: 50px; display: flex; gap: 10px; }
  .contacts { left: 380px; list-style: none; }
  .contacts li { display: flex; align-items: center; gap: 12px; }
  .icon { width: 14px; height: 14px; flex: none; fill: var(--gold); }

  .band { position: absolute; left: 0; bottom: 0; width: 700px; height: 40px; }
</style>
</head>
<body>
<main class="canvas">

  <section class="card card--front" aria-label="Business card front">
    <div class="brand">
      <span class="brand__mark"></span>
      <span class="brand__divider"></span>
      <span class="brand__name">Marlowe Law</span>
    </div>
    <p class="front__url">www.marlowelaw.com</p>
  </section>

  <section class="card card--back" aria-label="Business card back">
    <div class="brand">
      <span class="brand__mark"></span>
      <span class="brand__divider"></span>
      <span class="brand__name">Marlowe Law</span>
    </div>

    <div class="person">
      <p class="person__name">Sam Ellery</p>
      <p class="person__title">employee</p>
    </div>

    <div class="address">
      <svg class="icon" viewBox="0 0 16 16" aria-hidden="true"><path d="M8 1 1 8h2v7h4v-4h2v4h4V8h2z"/></svg>
      <p>P.O. Box 40217<br>Lakeview, WI 53012</p>
    </div>

    <ul class="contacts">
      <li><svg class="icon" viewBox="0 0 16 16" aria-hidden="true"><path d="M4 1 2 3c0 6 5 11 11 11l2-2-3-3-2 1c-2-1-3-2-4-4l1-2z"/></svg>555-014-2200</li>
      <li><svg class="icon" viewBox="0 0 16 16" aria-hidden="true"><path d="M4 1h6v4H4zM1 6h14v7H1zM4 9h8v5H4z"/></svg>555-014-2201</li>
      <li><svg class="icon" viewBox="0 0 16 16" aria-hidden="true"><path d="M1 3h14v10H1zM1 3l7 6 7-6"/></svg>sam.marlowelaw.com</li>
      <li><svg class="icon" viewBox="0 0 16 16" aria-hidden="true"><circle cx="8" cy="8" r="7"/></svg>www.marlowelaw.com</li>
    </ul>

    <svg class="band" viewBox="0 0 700 40" preserveAspectRatio="none" aria-hidden="true">
      <defs>
        <linearGradient id="band-gold" x1="0" x2="1" y1="0" y2="0">
          <stop offset="0" stop-color="var(--gold)"/>
          <stop offset="1" stop-color="var(--gold-light)"/>
        </linearGradient>
      </defs>
      <polygon points="0,8 340,8 372,40 0,40" fill="var(--band-grey)"/>
      <polygon points="360,16 700,16 700,40 384,40" fill="url(#band-gold)"/>
    </svg>
  </section>

</main>
</body>
</html>
```